Business Card design for Property Developer

We need a business card design for a Melbourne based Property Developer called "Kestrelmoor Holdings Pty Ltd".

We subdivide land and onsell to builders etc.

We already have a company logo, which is attached. Also I have attached the layout requirements from the printer. We would like a 2-sided design with one side displaying our logo by itself and the other with the required info, such as name, address, tel no., email, abn etc. The card will need to be used by 4 members of staff so name and contact details should be interchangable.
Updates

If possible, can you please write "name' "job position" "phone" "email" "address" on the card but leave them so I can add the details at a later time. Thank you. Also I plan on printing with UV spot printing as a background on the card. Keep this is mind when designing.

Thanks again.

Hello designers, please do not include pics of houses, house plansĀ or construction machinery etc as we really do not like the way it looks. Thank you.

Target Market(s)

Real Estate Agents, Land Owners, Local Council Departments, Govt Bodies, other Developers etc.

Industry/Entity Type

Business

Requirements
Must have
• 2-sided design with one side displaying our logo by itself and the other with the required info, such as name, address, tel no., email, abn etc.

```html
<!DOCTYPE html>
<html lang="en">
<head>
<meta charset="utf-8">
<title>Kestrelmoor Holdings – Business Card</title>
<link href="https://fonts.googleapis.com/css2?family=Orbitron:wght@700;800&display=swap" rel="stylesheet">
<style>
  :root {
    --backdrop: #e9ecef;
    --card-white: #ffffff;
    --blue-deep: #0d5fb8;
    --blue-mid: #1d86dc;
    --blue-light: #4fb6f2;
    --brand-red: #d3262e;
    --text-blue: #1a6fc4;
  }
  * { margin: 0; padding: 0; box-sizing: border-box; }
  html, body {
    width: 1200px;
    height: 900px;
    overflow: hidden;
    background: var(--backdrop);
  }
  .canvas {
    position: relative;
    width: 1200px;
    height: 900px;
    display: flex;
    flex-direction: column;
    align-items: center;
    justify-content: center;
    gap: 40px;
  }
  .card {
    position: relative;
    width: 700px;
    height: 400px;
    background: var(--card-white);
    box-shadow: 0 6px 18px rgba(0, 0, 0, 0.18);
    overflow: hidden;
  }
  .card-bands {
    position: absolute;
    inset: 0;
    width: 100%;
    height: 100%;
  }
  .card-content {
    position: absolute;
    inset: 0;
    display: flex;
    flex-direction: column;
    align-items: center;
    justify-content: center;
    font-family: "Orbitron", sans-serif;
  }
  .brand {
    display: flex;
    align-items: center;
    gap: 18px;
  }
  .brand-dot {
    width: 54px;
    height: 54px;
    border-radius: 50%;
    background: var(--blue-mid);
  }
  .brand-name {
    font-weight: 800;
    font-size: 30px;
    line-height: 1.15;
    color: var(--brand-red);
    letter-spacing: 1px;
    text-transform: uppercase;
  }
  .contact-list {
    list-style: none;
    text-align: center;
    color: var(--text-blue);
    font-weight: 700;
    font-size: 17px;
    letter-spacing: 1.5px;
    text-transform: uppercase;
    line-height: 2.35;
  }
</style>
</head>
<body>
<main class="canvas">

  <section class="card card-front" aria-label="Card front">
    <svg class="card-bands" viewBox="0 0 700 400" aria-hidden="true">
      <defs>
        <linearGradient id="bandBlue" x1="0" y1="0" x2="0" y2="1">
          <stop offset="0" stop-color="var(--blue-deep)"/>
          <stop offset="1" stop-color="var(--blue-mid)"/>
        </linearGradient>
      </defs>
      <path d="M0,0 H130 C55,95 55,305 130,400 H0 Z" fill="var(--blue-light)"/>
      <path d="M0,0 H108 C36,95 36,305 108,400 H0 Z" fill="url(#bandBlue)"/>
      <path d="M700,0 H570 C645,95 645,305 570,400 H700 Z" fill="var(--blue-light)"/>
      <path d="M700,0 H592 C664,95 664,305 592,400 H700 Z" fill="url(#bandBlue)"/>
    </svg>
    <div class="card-content">
      <div class="brand">
        <span class="brand-dot" aria-hidden="true"></span>
        <span class="brand-name">Kestrelmoor<br>Holdings</span>
      </div>
    </div>
  </section>

  <section class="card card-back" aria-label="Card back">
    <svg class="card-bands" viewBox="0 0 700 400" aria-hidden="true">
      <defs>
        <linearGradient id="bandBlueBack" x1="0" y1="0" x2="0" y2="1">
          <stop offset="0" stop-color="var(--blue-deep)"/>
          <stop offset="1" stop-color="var(--blue-mid)"/>
        </linearGradient>
      </defs>
      <path d="M0,0 H130 C55,95 55,305 130,400 H0 Z" fill="var(--blue-light)"/>
      <path d="M0,0 H108 C36,95 36,305 108,400 H0 Z" fill="url(#bandBlueBack)"/>
      <path d="M700,0 H570 C645,95 645,305 570,400 H700 Z" fill="var(--blue-light)"/>
      <path d="M700,0 H592 C664,95 664,305 592,400 H700 Z" fill="url(#bandBlueBack)"/>
    </svg>
    <div class="card-content">
      <ul class="contact-list">
        <li class="contact-name">Name Lastname</li>
        <li class="contact-position">Job Position</li>
        <li class="contact-phone">+61 3 9018 4427</li>
        <li class="contact-email">name@kestrelmoor.com</li>
        <li class="contact-address">Melbourne VIC, Address Line</li>
      </ul>
    </div>
  </section>

</main>
</body>
</html>
```